New Card

Photography business
I want a sleek simple card that screams rich and classy. Black/Gold or silver font. No photos or images but would love a new logo When I hand someone my card I want compliments
Updates
My fiancé reminded me in 5 short months my name will change so I have changed my name to Colleen Marwick
Also my BRAND is Lantern Bloom Photography, not my name. Thanks
Industry/Entity Type
Business
Contact Information for Business Card
Lantern Bloom Photography
Colleen Marwick-owner
482 W. Thornbury Rd.
Alder Falls, NJ 08321
(555)555-0142
colleen@lanternbloomstudio.example
Look and feel
Each slider illustrates characteristics of the customer's brand and the style your logo design should communicate.

```html
<!DOCTYPE html>
<html lang="en">
<head>
<meta charset="utf-8">
<title>Lantern Bloom Photography – Business Card</title>
<link rel="stylesheet" href="https://fonts.googleapis.com/css2?family=Fira+Sans+Condensed:wght@500;600&family=Lato:wght@300;400;700&display=swap">
<style>
  :root {
    --page: #d9d9d9;
    --card: #2a2c30;
    --ink-light: #f2f2f2;
    --gold: #f2ae1c;
    --ink-dark: #1f1f22;
    --rule: #b98a22;
  }
  * { box-sizing: border-box; margin: 0; padding: 0; }
  html, body { width: 1200px; height: 926px; overflow: hidden; }
  body {
    background: var(--page);
    display: flex;
    flex-direction: column;
    align-items: center;
    justify-content: center;
    gap: 46px;
    font-family: "Lato", sans-serif;
  }
  .card {
    width: 700px;
    height: 400px;
    background: var(--card);
    position: relative;
    overflow: hidden;
  }

  /* Back side */
  .card-back {
    display: flex;
    flex-direction: column;
    align-items: center;
    justify-content: center;
    gap: 18px;
  }
  .brand-dot {
    width: 44px; height: 44px;
    border: 2px solid var(--gold);
    border-radius: 50%;
  }
  .brand-name {
    color: var(--ink-light);
    font-weight: 300;
    text-align: center;
    line-height: 1;
  }
  .brand-name .main { display: block; font-size: 48px; letter-spacing: 1px; text-transform: uppercase; }
  .brand-name .sub { display: block; font-size: 16px; font-weight: 300; letter-spacing: 6px; text-transform: uppercase; margin-top: 10px; text-align: right; }

  /* Front side */
  .card-front { padding: 48px 50px 0; }
  .rule-top {
    position: relative;
    height: 20px;
    display: flex;
    align-items: center;
  }
  .rule-top::before {
    content: ""; position: absolute; left: 0; right: 0; top: 50%;
    height: 1px; background: var(--rule);
  }
  .rule-top .mark {
    position: relative;
    margin: 0 auto;
    width: 20px; height: 20px;
    border: 2px solid var(--gold);
    border-radius: 50%;
    background: var(--card);
    box-shadow: 0 0 0 8px var(--card);
  }
  .owner {
    font-family: "Fira Sans Condensed", sans-serif;
    font-weight: 600;
    font-size: 42px;
    letter-spacing: 1px;
    text-transform: uppercase;
    color: var(--ink-light);
    margin-top: 20px;
    line-height: 1.1;
  }
  .owner .role { color: var(--gold); }
  .phone {
    font-weight: 700;
    font-size: 60px;
    letter-spacing: 2px;
    color: var(--ink-light);
    line-height: 1.15;
    margin-top: 8px;
  }
  .email-row {
    display: flex;
    align-items: center;
    gap: 12px;
    margin-top: 24px;
  }
  .email-row .line { flex: 1; height: 1px; background: var(--rule); }
  .email {
    font-size: 18px;
    color: var(--ink-light);
    letter-spacing: 0.5px;
  }
  .address-band {
    position: absolute;
    left: 0; right: 0; bottom: 0;
    height: 74px;
    background: var(--gold);
    display: flex;
    align-items: center;
    justify-content: center;
    font-family: "Fira Sans Condensed", sans-serif;
    font-weight: 500;
    font-size: 23px;
    letter-spacing: 2.5px;
    text-transform: uppercase;
    color: var(--ink-dark);
  }
</style>
</head>
<body>
  <section class="card card-back" aria-label="Card back">
    <span class="brand-dot"></span>
    <h1 class="brand-name">
      <span class="main">Lantern Bloom</span>
      <span class="sub">Photography</span>
    </h1>
  </section>

  <section class="card card-front" aria-label="Card front">
    <div class="rule-top"><span class="mark"></span></div>
    <p class="owner">Colleen Marwick-<span class="role">Owner</span></p>
    <p class="phone">(555)555-0142</p>
    <div class="email-row">
      <span class="line"></span>
      <span class="email">colleen@lanternbloomstudio.example</span>
      <span class="line"></span>
    </div>
    <div class="address-band">482 W. Thornbury Rd. Alder Falls, NJ 08321</div>
  </section>
</body>
</html>
```